Brookvale Holdings Ltd - Logo and Business Card

Create a logo and business card design for our new company.

Canadian private investment company with holdings in Saskatchewan Oil and real-estate.

Target Market(s)

Investors

Industry/Entity Type

Finance

Contact Information for Business Card

Name - Dominic Harlow
Position - President
Phone - 306.482.7159
Website - www.brookvaleholdings.ca

Logo Text

Today. Tomorrow. Together. (Tag Line)

Colors

Designer to choose colors to be used in the design.

Requirements
Must have
• Logo Must Have - Type Font only
• Must be modern, professional and stand out from the crowd.
Nice to have
• Don't have any, blank slate.

```html
<!DOCTYPE html>
<html lang="en">
<head>
<meta charset="utf-8">
<title>Brookvale Holdings Ltd – Business Card</title>
<link href="https://fonts.googleapis.com/css2?family=Open+Sans:wght@400;600;700&display=swap" rel="stylesheet">
<style>
  :root {
    --page-bg: #e6e6e6;
    --card-dark: #1f1f1f;
    --card-light: #ffffff;
    --ink: #3a3a3a;
    --ink-soft: #4a4a4a;
    --accent: #7cc242;
    --logo-on-dark: #6b6b6b;
  }
  * { margin: 0; padding: 0; box-sizing: border-box; }
  html, body {
    width: 1200px; height: 1000px; overflow: hidden;
    background: var(--page-bg);
    font-family: "Open Sans", Arial, sans-serif;
  }
  .card {
    position: absolute; left: 250px; width: 700px; height: 400px;
    box-shadow: 0 6px 18px rgba(0,0,0,.18);
  }
  .card--back { top: 50px; background: var(--card-dark); }
  .card--front { top: 520px; background: var(--card-light); color: var(--ink); }

  .wordmark {
    position: absolute; left: 0; right: 0; text-align: center;
    font-weight: 600; line-height: 1;
  }
  .wordmark__name { display: block; font-size: 56px; letter-spacing: 1px; }
  .wordmark__suffix { display: block; font-size: 19px; letter-spacing: 6px; margin-top: 8px; }
  .card--back .wordmark { top: 145px; color: var(--logo-on-dark); }
  .card--front .wordmark { top: 50px; color: var(--ink); }

  .identity {
    position: absolute; top: 205px; right: 385px; text-align: right;
  }
  .identity__name { font-size: 28px; font-weight: 700; color: var(--ink); line-height: 1.2; }
  .identity__role { font-size: 24px; font-weight: 600; color: var(--accent); line-height: 1.2; }

  .divider {
    position: absolute; left: 335px; top: 210px; width: 2px; height: 66px; background: var(--ink);
  }
  .contacts {
    position: absolute; left: 350px; top: 205px; list-style: none;
    font-size: 18px; color: var(--ink-soft);
  }
  .contacts li { display: flex; align-items: center; height: 25px; }
  .contacts svg { width: 14px; height: 14px; margin-right: 14px; fill: var(--accent); flex: none; }
  .contacts .web-core { color: var(--accent); }

  .address {
    position: absolute; left: 0; right: 0; top: 330px;
    display: flex; justify-content: center; align-items: center;
    font-size: 18px; color: var(--ink-soft);
  }
  .address svg { width: 16px; height: 20px; margin-right: 8px; fill: var(--accent); }
</style>
</head>
<body>
  <section class="card card--back" aria-label="Business card back">
    <div class="wordmark">
      <span class="wordmark__name">BROOKVALE</span>
      <span class="wordmark__suffix">HOLDINGS LTD</span>
    </div>
  </section>

  <section class="card card--front" aria-label="Business card front">
    <div class="wordmark">
      <span class="wordmark__name">BROOKVALE</span>
      <span class="wordmark__suffix">HOLDINGS LTD</span>
    </div>

    <div class="identity">
      <p class="identity__name">Dominic Harlow</p>
      <p class="identity__role">President</p>
    </div>

    <div class="divider"></div>

    <ul class="contacts">
      <li>
        <svg viewBox="0 0 24 24"><path d="M6.6 10.8a15.1 15.1 0 0 0 6.6 6.6l2.2-2.2c.3-.3.7-.4 1-.2 1.1.4 2.3.6 3.6.6.6 0 1 .4 1 1V20c0 .6-.4 1-1 1A17 17 0 0 1 3 4c0-.6.4-1 1-1h3.5c.6 0 1 .4 1 1 0 1.3.2 2.5.6 3.6.1.3 0 .7-.2 1z"/></svg>
        306.482.7159
      </li>
      <li>
        <svg viewBox="0 0 24 24"><path d="M2 5h20v14H2z M2 5l10 8 10-8" stroke="#fff" stroke-width="1.5"/></svg>
        dharlow@brookvaleholdings.ca
      </li>
      <li>
        <svg viewBox="0 0 24 24"><circle cx="12" cy="12" r="10"/><path d="M2 12h20M12 2c3 3 3 17 0 20M12 2c-3 3-3 17 0 20" stroke="#fff" stroke-width="1.3" fill="none"/></svg>
        <span>www.<span class="web-core">brookvaleholdings</span>.ca</span>
      </li>
    </ul>

    <p class="address">
      <svg viewBox="0 0 16 20"><path d="M8 0a8 8 0 0 0-8 8c0 6 8 12 8 12s8-6 8-12a8 8 0 0 0-8-8zm0 11a3 3 0 1 1 0-6 3 3 0 0 1 0 6z"/></svg>
      Your Street Address, Singapore, 1234
    </p>
  </section>
</body>
</html>
```